Builder Website Brackwell Construction

Hi,
Brackwell Construction is a domestic builder on the Gold Coast specializing in new homes, townhouses, duplexes and high end renovations.
Brackwell Construction can make your dream new home or development a reality. Whether you already have plans or require a complete design and construct project service, Brackwell Construction will make your project a stress free experience.
We offer design, town planning, certification and construction services.

Target Market(s)

Anyone looking to build.

Industry/Entity Type

Building

Coding

Coded - Design and coding required

Font styles to use
Other font styles liked:
• Match logo

Colors

Designer to choose colors to be used in the design.

Requirements
Must have
• Attractive home page with logo etc.
• About us page
• Gallery page
• Services Page
• Contact us page

```html
<!DOCTYPE html>
<html lang="en">
<head>
<meta charset="utf-8">
<title>Brackwell Construction</title>
<link href="https://fonts.googleapis.com/css2?family=Lato:wght@300;400;700&display=swap" rel="stylesheet">
<style>
:root{
  --bg:#000;
  --ink:#fff;
  --muted:#cfcfcf;
  --line:#e6e6e6;
  --hero-a:#d9dde0;
  --hero-b:#8e9498;
}
*{box-sizing:border-box;margin:0;padding:0}
html,body{width:1200px;height:3719px;overflow:hidden;background:var(--bg)}
body{position:relative;font-family:"Lato",Arial,sans-serif;color:var(--ink)}
.abs{position:absolute}
.btn{position:absolute;border:2px solid var(--ink);color:var(--ink);font-size:14px;letter-spacing:.5px;text-transform:uppercase;display:flex;align-items:center;justify-content:center}
.btn--solid{background:var(--ink);color:#000}
.photo{position:absolute}
.side-title{position:absolute;transform:rotate(-90deg);transform-origin:left top;font-size:29px;letter-spacing:2px;white-space:nowrap}
.bracket{position:absolute;border:2px solid var(--line)}
p.copy{font-size:13.5px;line-height:1.5}

/* header */
.brand{left:0;width:1200px;top:6px;text-align:center}
.brand__mark{width:58px;height:58px;border:2px solid var(--ink);border-radius:50%;margin:0 auto 4px}
.brand__name{font-size:18px;letter-spacing:1px}
.nav{top:116px;left:0;width:1200px;display:flex;justify-content:center;gap:55px;font-size:15px;letter-spacing:1.5px}
.nav a{color:var(--ink);text-decoration:none;position:relative;padding-bottom:10px}
.nav a.is-active:after{content:"";position:absolute;left:0;right:0;bottom:-14px;height:3px;background:var(--ink)}

/* hero */
.hero{left:79px;top:161px;width:1042px;height:513px;background:linear-gradient(100deg,#5f6468 0%,var(--hero-a) 45%,#f1f1ef 70%,var(--hero-b) 100%)}
.hero__title{left:151px;top:436px;font-size:36px;font-weight:700;line-height:1.25;letter-spacing:.5px}

/* about */
.about__img{left:620px;top:637px;width:476px;height:389px;background:linear-gradient(135deg,#eaeaea,#7c7c7c 55%,#cfcfcf)}
.about__text{left:151px;top:742px;width:452px}
.about__text p+p{margin-top:14px}

/* specialize */
.spec__title{left:0;width:1200px;top:1140px;text-align:center;font-size:28px;letter-spacing:1px}
.spec__stem{left:599px;top:1180px;width:2px;height:44px;background:var(--line)}
.spec{top:1262px;width:240px}
.spec__num{position:absolute;left:-38px;top:6px;width:40px;height:40px;border-radius:50%;background:var(--ink);color:#000;font-weight:700;font-size:16px;display:flex;align-items:center;justify-content:center}
.spec__name{font-size:20px;margin-left:8px}
.spec p{margin-left:8px;width:195px;margin-top:2px}

/* services */
.svc{top:1611px;width:228px}
.svc__img{height:226px}
.svc__tag{position:absolute;left:0;top:135px;width:34px;height:160px;background:var(--ink)}
.svc__tag span{position:absolute;left:8px;bottom:6px;transform:rotate(-90deg);transform-origin:left top;color:#000;font-size:12px;white-space:nowrap;top:auto;translate:0 0}
.svc p{margin:8px 0 0 46px;font-size:13.5px}

/* projects */
.proj__feature-text{left:600px;top:2290px;width:471px;text-align:center}
.proj__feature-text h3{font-size:28px;font-weight:400;letter-spacing:.5px;margin-bottom:8px}
.proj__feature-text p{width:260px;margin:0 auto}

/* contact */
.field{position:absolute;border:2px solid var(--line);font-size:11.5px;letter-spacing:.5px;padding:12px 0 0 18px;text-transform:uppercase}

/* footer */
.foot h4{position:absolute;font-size:16px;font-weight:400;letter-spacing:1px}
.foot__rule{position:absolute;width:48px;height:1px;background:var(--muted)}
.foot__list{position:absolute;list-style:none;font-size:13px;line-height:22px}
.social{left:82px;top:3588px;display:flex;gap:14px}
.social i{display:block;width:18px;height:18px;border:1.5px solid var(--ink);border-radius:3px}
.insta{left:664px;top:3505px;display:grid;grid-template-columns:repeat(3,48px);gap:5px}
.insta b{height:36px;display:block}
.legal{top:3668px;font-size:13px}
</style>
</head>
<body>

<header>
  <div class="abs brand">
    <div class="brand__mark"></div>
    <div class="brand__name">Brackwell</div>
  </div>
  <nav class="abs nav">
    <a class="is-active">Home</a><a>About</a><a>Services</a><a>Projects</a><a>Contact</a>
  </nav>
</header>

<section class="hero-block">
  <div class="photo hero" role="img" aria-label="Bright white kitchen interior with island and pendant lights"></div>
  <h1 class="abs hero__title">LOOKING FOR<br>QUALITY CONSTRUCTOR</h1>
  <div class="btn" style="left:156px;top:565px;width:171px;height:47px;">Contact Us</div>
</section>

<section class="about">
  <div class="bracket" style="left:89px;top:726px;width:508px;height:70px;border-right:none;border-bottom:none;"></div>
  <div class="side-title" style="left:76px;top:958px;">ABOUT US</div>
  <div class="abs about__text">
    <p class="copy">Lorem Ipsum is simply dummy text of the printing and typesetting industry. Lorem Ipsum has been the industry's standard dummy text ever since the 1500s, when an unknown printer took a galley of type and scrambled it to make a type specimen book.</p>
    <p class="copy">It has survived not only five centuries, but also the leap into electronic typesetting, remaining essentially unchanged.</p>
  </div>
  <div class="btn" style="left:154px;top:910px;width:168px;height:47px;">Read More</div>
  <div class="photo about__img" role="img" aria-label="Modern architectural facade with angled slats"></div>
</section>

<section class="specialize">
  <h2 class="abs spec__title" style="font-weight:400">OUR SPECIALIZE</h2>
  <div class="abs spec__stem"></div>
  <div class="abs spec" style="left:128px"><div class="spec__num">01</div><div class="spec__name">NEW HOMES</div><p class="copy">Lorem Ipsum is simply dummy text of the printing and typesetting industry.</p></div>
  <div class="abs spec" style="left:394px"><div class="spec__num">02</div><div class="spec__name">TOWN PLANNNING</div><p class="copy">Lorem Ipsum is simply dummy text of the printing and typesetting industry.</p></div>
  <div class="abs spec" style="left:659px"><div class="spec__num">03</div><div class="spec__name">DUPLEXES</div><p class="copy">Lorem Ipsum is simply dummy text of the printing and typesetting industry.</p></div>
  <div class="abs spec" style="left:934px"><div class="spec__num">04</div><div class="spec__name">RENOVATIONS</div><p class="copy">Lorem Ipsum is simply dummy text of the printing and typesetting industry.</p></div>
</section>

<section class="services">
  <div class="bracket" style="left:89px;top:1524px;width:508px;height:40px;border-left:none;border-bottom:none;"></div>
  <div class="abs" style="left:89px;top:1524px;width:2px;height:22px;background:var(--line)"></div>
  <div class="side-title" style="left:76px;top:1750px;">OUR SERVICES</div>

  <div class="abs svc" style="left:164px">
    <div class="photo svc__img" style="position:relative;background:linear-gradient(135deg,#cfd3c8,#4f8a3a 60%,#2d5a25)" role="img" aria-label="Hand placing model buildings on a town plan"></div>
    <div class="svc__tag"><span style="left:9px;top:150px">TOWN PLANNING</span></div>
    <p>Lorem Ipsum is simply dummy text of the printing and typesetting industry.</p>
  </div>
  <div class="abs svc" style="left:404px">
    <div class="photo svc__img" style="position:relative;background:linear-gradient(135deg,#f2c230,#e9e9e6 40%,#bfc2c4)" role="img" aria-label="Hands working on blueprints beside a hard hat"></div>
    <div class="svc__tag"><span style="left:9px;top:70px">DESIGN</span></div>
    <p>Lorem Ipsum is simply dummy text of the printing and typesetting industry.</p>
  </div>
  <div class="abs svc" style="left:647px">
    <div class="photo svc__img" style="position:relative;background:linear-gradient(135deg,#2a2a2a,#cfc6b8 55%,#f3f1ec)" role="img" aria-label="Business person giving a thumbs up"></div>
    <div class="svc__tag"><span style="left:9px;top:130px">CERTIFICATION</span></div>
    <p>Lorem Ipsum is simply dummy text of the printing and typesetting industry.</p>
  </div>
  <div class="abs svc" style="left:887px">
    <div class="photo svc__img" style="position:relative;background:linear-gradient(135deg,#e8eef3,#c8914f 55%,#a06a34)" role="img" aria-label="Timber house frame under construction"></div>
    <div class="svc__tag"><span style="left:9px;top:130px">CONSTRUCTION</span></div>
    <p>Lorem Ipsum is simply dummy text of the printing and typesetting industry.</p>
  </div>

  <div class="btn" style="left:179px;top:1929px;width:171px;height:47px;">Read More</div>
  <div class="btn" style="left:423px;top:1929px;width:171px;height:47px;">Read More</div>
  <div class="btn" style="left:662px;top:1929px;width:171px;height:47px;">Read More</div>
  <div class="btn" style="left:907px;top:1929px;width:171px;height:47px;">Read More</div>
</section>

<section class="projects">
  <div class="bracket" style="left:600px;top:2087px;width:472px;height:40px;border-right:none;border-bottom:none;"></div>
  <div class="abs" style="left:1070px;top:2087px;width:2px;height:22px;background:var(--line)"></div>
  <div class="side-title" style="left:1092px;top:2400px;">RECENTLY&nbsp; PROJECTS</div>

  <div class="photo" style="left:82px;top:2172px;width:327px;height:143px;background:linear-gradient(135deg,#a9c3d8,#e7e7e4 50%,#6f6f6f)" role="img" aria-label="Row of white terrace houses"></div>
  <div class="photo" style="left:416px;top:2172px;width:176px;height:143px;background:linear-gradient(135deg,#f4f4f2,#c9cfc4)" role="img" aria-label="Bright interior with large window"></div>
  <div class="photo" style="left:82px;top:2325px;width:327px;height:273px;background:linear-gradient(135deg,#f0efeb,#d9d4ce 60%,#b7aaa3)" role="img" aria-label="White living room with sofa and kitchen"></div>
  <div class="photo" style="left:416px;top:2325px;width:176px;height:273px;background:linear-gradient(160deg,#2f8fd6,#d9dee2 50%,#3e6b3a)" role="img" aria-label="Two-storey house with porch under blue sky"></div>
  <div class="photo" style="left:600px;top:2172px;width:471px;height:426px;background:linear-gradient(180deg,#3f4a55,#2e3a36 50%,#3a3333 75%,#4a2d2d)" role="img" aria-label="Residential street with houses and red flowers"></div>
  <div class="abs proj__feature-text">
    <h3>PROJECT NAME</h3>
    <p class="copy">Lorem Ipsum is simply dummy text of the printing and typesetting industry. Lorem Ipsum has been the industry's standard dummy text ever since the 1500s.</p>
    <svg width="34" height="34" viewBox="0 0 34 34" style="margin-top:6px" aria-hidden="true"><circle cx="14" cy="14" r="10" fill="none" stroke="#fff" stroke-width="2"/><path d="M21 21l9 9M10 14h8M14 10v8" stroke="#fff" stroke-width="2"/></svg>
  </div>
  <div class="btn" style="left:516px;top:2648px;width:168px;height:49px;">View More</div>
</section>

<section class="contact">
  <div class="bracket" style="left:89px;top:2846px;width:508px;height:40px;border-left:none;border-bottom:none;"></div>
  <div class="abs" style="left:89px;top:2846px;width:2px;height:22px;background:var(--line)"></div>
  <div class="side-title" style="left:76px;top:3072px;">CONTACT&nbsp; US</div>
  <div class="field" style="left:136px;top:2947px;width:320px;height:50px;">Full Name</div>
  <div class="field" style="left:468px;top:2947px;width:318px;height:50px;">Email Address</div>
  <div class="field" style="left:796px;top:2947px;width:320px;height:50px;">Phone Number</div>
  <div class="field" style="left:136px;top:3012px;width:980px;height:169px;">Massage</div>
  <div class="btn btn--solid" style="left:136px;top:3195px;width:169px;height:50px;">View More</div>
</section>

<footer class="foot">
  <div class="abs" style="left:95px;top:3396px;width:46px;height:46px;border:2px solid var(--ink);border-radius:50%"></div>
  <div class="abs" style="left:80px;top:3448px;font-size:18px">Brackwell</div>
  <p class="abs copy" style="left:82px;top:3500px;width:260px;font-size:13px">Lorem Ipsum is simply dummy text of the printing and typesetting industry.</p>
  <div class="abs" style="left:82px;top:3552px;font-size:13px;text-decoration:underline">READ MORE</div>
  <div class="abs social"><i></i><i></i><i></i><i></i><i></i></div>

  <h4 style="left:451px;top:3394px">QUICK LINK</h4>
  <div class="foot__rule" style="left:451px;top:3456px"></div>
  <ul class="foot__list" style="left:451px;top:3502px"><li>Home</li><li>About</li><li>Services</li><li>Projects</li><li>Contact</li></ul>

  <h4 style="left:659px;top:3394px">INSTAGARM</h4>
  <div class="foot__rule" style="left:659px;top:3456px"></div>
  <div class="abs insta">
    <b style="background:linear-gradient(135deg,#9fb4c6,#e3e3df)"></b>
    <b style="background:linear-gradient(135deg,#4d7aa8,#d8d8d4)"></b>
    <b style="background:linear-gradient(135deg,#2d6fb8,#cfd5da)"></b>
    <b style="background:linear-gradient(135deg,#eeeeea,#bdb4ad)"></b>
    <b style="background:linear-gradient(135deg,#2f8fd6,#d9dee2)"></b>
    <b style="background:linear-gradient(135deg,#3f4a55,#4a2d2d)"></b>
  </div>

  <h4 style="left:892px;top:3394px">QUICK LINK</h4>
  <div class="foot__rule" style="left:892px;top:3456px"></div>
  <ul class="foot__list" style="left:892px;top:3502px;font-size:12.5px">
    <li><svg width="12" height="12" viewBox="0 0 12 12" style="margin:0 8px -1px 0"><path d="M2 1l3 1 0 3-1 1c1 2 2 3 3 3l1-1 3 0 1 3c-6 1-11-4-10-10z" fill="none" stroke="#fff"/></svg>(+012)-555-014-9</li>
    <li><svg width="12" height="12" viewBox="0 0 12 12" style="margin:0 8px -1px 0"><rect x="1" y="3" width="10" height="7" fill="none" stroke="#fff"/><path d="M3 3V1h6v2" fill="none" stroke="#fff"/></svg>(+012)-555-014-0</li>
    <li><svg width="12" height="12" viewBox="0 0 12 12" style="margin:0 8px -1px 0"><rect x="1" y="2" width="10" height="8" fill="none" stroke="#fff"/><path d="M1 2l5 4 5-4" fill="none" stroke="#fff"/></svg>info@brackwellconstruction.com</li>
    <li><svg width="12" height="12" viewBox="0 0 12 12" style="margin:0 8px -1px 0"><path d="M6 11C3 7 2 5.5 2 4a4 4 0 018 0c0 1.5-1 3-4 7z" fill="none" stroke="#fff"/><circle cx="6" cy="4" r="1.3" fill="#fff"/></svg>418 Harlow Ave.<br><span style="margin-left:20px">Ridgeton, MT 59000</span></li>
  </ul>

  <div class="abs" style="left:79px;top:3642px;width:1042px;height:1px;background:#555"></div>
  <div class="abs legal" style="left:79px">Copyright © 2018 Brackwell construction. All rights reserved.</div>
  <div class="abs legal" style="left:900px;width:221px;text-align:right">Privacy Policy - Terms &amp; conditions</div>
</footer>

</body>
</html>
```